Brintell's Business Card

I need some designs for a new business card including the new logo attached. An old example of our business card is also attached to show all the data that should be included on the new design.
**I added some more examples someone had mocked up**

Contact Information for Business Card

Should include all info on other examples uploaded.

```html
<!DOCTYPE html>
<html lang="en">
<head>
<meta charset="utf-8">
<title>Brintell's Business Card</title>
<link rel="stylesheet" href="https://fonts.googleapis.com/css2?family=Montserrat:wght@500;600;700&display=swap">
<style>
  :root {
    --brand-blue: #1572b6;
    --brand-red: #e5322d;
    --ink: #1c1c1c;
    --paper: #ffffff;
    --backdrop: #ececec;
  }
  * { box-sizing: border-box; margin: 0; padding: 0; }
  html, body { width: 1200px; height: 900px; overflow: hidden; }
  body {
    background: var(--backdrop);
    font-family: "Montserrat", Arial, sans-serif;
    position: relative;
  }
  .card {
    position: absolute;
    left: 297px;
    width: 604px;
    height: 346px;
    background: var(--paper);
  }
  .card--front { top: 80px; }
  .card--back { top: 474px; }

  .brand { position: absolute; display: flex; align-items: center; }
  .brand__dot {
    flex: none;
    border-radius: 50%;
    background: var(--brand-red);
  }
  .brand__text { display: flex; flex-direction: column; }
  .brand__name {
    color: var(--brand-blue);
    font-weight: 600;
    line-height: 1;
    white-space: nowrap;
  }
  .brand__tagline {
    color: var(--brand-red);
    font-weight: 600;
    white-space: nowrap;
  }

  .card--front .brand { left: 0; right: 0; top: 118px; justify-content: center; gap: 14px; }
  .card--front .brand__dot { width: 30px; height: 30px; }
  .card--front .brand__name { font-size: 48px; letter-spacing: 0.5px; }
  .card--front .brand__tagline { font-size: 13.5px; margin-top: 6px; }

  .service-area {
    position: absolute;
    top: 272px;
    left: 0; right: 0;
    text-align: center;
    color: var(--brand-blue);
    font-size: 14.5px;
    font-weight: 500;
  }
  .band {
    position: absolute;
    left: 0; right: 0;
    height: 38px;
    background: var(--brand-blue);
    color: var(--paper);
    font-size: 15px;
    font-weight: 500;
    display: flex;
    align-items: center;
    justify-content: center;
    gap: 10px;
    white-space: nowrap;
  }
  .card--front .band { top: 298px; }
  .card--back .band { top: 293px; }
  .band__sep { font-size: 12px; }

  .card--back .brand { left: 40px; top: 142px; gap: 8px; }
  .card--back .brand__dot { width: 18px; height: 18px; }
  .card--back .brand__name { font-size: 30px; }
  .card--back .brand__tagline { font-size: 8.5px; margin-top: 4px; }

  .divider {
    position: absolute;
    left: 298px;
    top: 128px;
    width: 2px;
    height: 80px;
    background: var(--brand-red);
  }
  .contact { position: absolute; left: 313px; top: 129px; }
  .contact__name { font-size: 19px; font-weight: 700; color: var(--brand-blue); letter-spacing: 0.2px; }
  .contact__name span { color: var(--brand-red); }
  .contact__line {
    display: flex;
    align-items: center;
    gap: 5px;
    margin-top: 7px;
    font-size: 15px;
    font-weight: 500;
    color: var(--ink);
  }
  .contact__line:first-of-type { margin-top: 10px; }
  .contact__icon { width: 14px; height: 12px; flex: none; }
</style>
</head>
<body>
  <section class="card card--front">
    <div class="brand">
      <span class="brand__dot"></span>
      <div class="brand__text">
        <span class="brand__name">BRINTELL'S</span>
        <span class="brand__tagline">AIR CONDITIONING &amp; HEATING SERVICE</span>
      </div>
    </div>
    <p class="service-area">SERVES MILLBROOK, IA &amp; SURROUNDING AREAS</p>
    <div class="band">CALL TODAY FOR ALL YOUR HVAC, REFRIGERATION &amp; PLUMBING NEEDS</div>
  </section>

  <section class="card card--back">
    <div class="brand">
      <span class="brand__dot"></span>
      <div class="brand__text">
        <span class="brand__name">BRINTELL'S</span>
        <span class="brand__tagline">AIR CONDITIONING &amp; HEATING SERVICE</span>
      </div>
    </div>
    <div class="divider"></div>
    <div class="contact">
      <p class="contact__name">DALE <span>BRINTELL</span></p>
      <p class="contact__line">
        <svg class="contact__icon" viewBox="0 0 14 12" aria-hidden="true">
          <path d="M1 4 Q7 0 13 4 L12 5.5 L9.5 4.5 L9.5 3.5 Q7 2.8 4.5 3.5 L4.5 4.5 L2 5.5 Z" fill="#e5322d"/>
          <rect x="3" y="6" width="8" height="5.5" rx="1" fill="#e5322d"/>
        </svg>
        555.014.2290
      </p>
      <p class="contact__line">
        <svg class="contact__icon" viewBox="0 0 14 12" aria-hidden="true">
          <rect x="0.5" y="1.5" width="13" height="9" fill="#e5322d"/>
          <path d="M0.5 1.5 L7 7 L13.5 1.5" fill="none" stroke="#fff" stroke-width="1.2"/>
        </svg>
        hvacbrintell@mailbox.com
      </p>
    </div>
    <div class="band">
      <span>LICENSED &amp; INSURED</span>
      <span class="band__sep">|</span>
      <span>FAMILY OWNED &amp; OPERATED</span>
    </div>
  </section>
</body>
</html>
```